Web Design Project: Facility Management company

Hi! We need a new website.

Our current website: http://www.vireo-trade.ru/ and we don-t like it. =)
The structure of our company has changed and now we don't need "cleaning" and "engeneering" on this site.

We are facility management company in Russia. So we provide integrated service solutions specific to industrial services: maintenance, repair, etc. of engineering systems.
More services:
Energy planning
Automation
Audit
Statements with regulators
Video surveillance
Central heating
Security systems
Welding
Management of subcontractors
Electrical installation and service needs
Reception
Catering

Visitors:
* Managers in the field of commercial real estate
* Chief engineers
* TOP managers of large companies, malls, factories...
+ their subordinates
* Small% of applicants.

Here you can see some websites/patterns we liked:
http://www.kobalmire.ru/ (This is our competitor’s site, so our site shouldn’t be an exact copy))))
http://www.dwatqo.ru/
http://www.layoutfarrow.com/demo/24296.html
http://www.layoutfarrow.com/website-templates/10145.html

Style:
Light, hi-tech/minimalizm, the color palette should be based on the original site colors (Green + black + white). http://www.vireo-trade.ru/

Estimated sitemap:
1. Home
2. About Us
3. Company's policy
4. History + Achievements.
5. Certificates
6. Map of presence (Here you can use sample map in file "our projects")
7. Services
8. Portfolio
9. News or blog
10. Jobs
11. Contacts - with the feedback form (or the function "call to order")
12. English

Need a design pages: main page, page 404. The rest of the page could be created by general pattern.

Logo, navigation bar and contacts should be visible on all pages of a site.
Flash animation elements and buttons, etc. - not needed.

* We need to develop 3 websites, so we are looking for a long term cooperation.
Looking forward to your creativity =)

Must Have:
Clear, intuitive structure of web pages.
In the center - of pictures reflecting our main services (industrial theme). May be in rotation.
BUT! This banner (central picture) should not be a huge one =)
All relevant information should be visible at once without scrolling.

A possibility to place media files (presentations, video ...) and 2 banner links on the main page.

Font should be available in Cyrillic.
Updates

IMPORTANT!

Please notice that in thisdesign we don't need "cleaning" and "engeneering" on this site.

So don't use old block of 4pictures from our current website. We don't need it anymore. 

Thestructure of our company has changed and now we need some links (may be banners,may be something else) to our future cleaning website as well as engeneeringwebsite.
It should look like seperate (partner) companies, not like our sevices.

Regards, Vera.

Please don't forget that we need bilingual site.

So define language changing tool in your designs.

Industry/Entity Type

Industrial

```html
<!DOCTYPE html>
<html lang="en">
<head>
<meta charset="utf-8">
<title>Vireo Trade — Facility Management</title>
<link href="https://fonts.googleapis.com/css2?family=Open+Sans:wght@400;600;700&display=swap" rel="stylesheet">
<style>
:root{
  --dark:#232323;
  --green:#6d8a24;
  --green-light:#d3e183;
  --hero-text:#d6e48f;
  --orange:#f29a17;
  --text:#444;
  --white:#fff;
}
*{margin:0;padding:0;box-sizing:border-box}
html,body{width:1200px;height:1045px;overflow:hidden}
body{font-family:"Open Sans",Arial,sans-serif;color:var(--text);background:var(--white);position:relative}
.abs{position:absolute}

.topbar{left:0;top:0;width:1200px;height:47px;background:var(--dark)}
.nav{left:110px;top:5px;height:42px;display:flex;list-style:none}
.nav li{height:42px;display:flex;align-items:center;padding:0 12.5px;font-size:12.6px;color:#eee;border-right:1px solid #3a3a3a;text-transform:uppercase;white-space:nowrap}
.nav li.active{background:linear-gradient(#f9fbef,#dfe9b4);color:var(--green);padding:0 16px;font-weight:600}

.stage{left:0;top:47px;width:1200px;height:441px;background:linear-gradient(#fafcf2 0%,#eef5d4 45%,#d4e39c 100%)}

.brand{left:112px;top:90px;display:flex;align-items:center;gap:12px;font-size:34px;font-weight:600;letter-spacing:5px;color:#111}
.brand-mark{width:22px;height:22px;background:var(--green-light)}

.search{left:778px;top:74px;width:207px;height:28px;border:1px solid #d8d8d8;background:#fff;font-size:11px;color:#888;padding:6px 9px}
.search-btn{left:984px;top:74px;width:27px;height:28px;background:#7f9d2e}
.lang{left:1024px;top:74px;width:67px;height:28px;background:var(--orange);color:#fff;font-size:13px;font-weight:600;text-align:center;line-height:28px;border-radius:2px}
.help{left:614px;top:119px;font-size:24px;color:#111;display:flex;align-items:center;gap:10px;white-space:nowrap}
.help b{font-weight:600}

.hero-frame{left:109px;top:173px;width:982px;height:358px;background:#f4f4f4;border:1px solid #ddd;border-radius:3px}
.hero{left:126px;top:190px;width:948px;height:324px;overflow:hidden;background:radial-gradient(circle at 75% 40%,#4a4a4a,#262626 70%)}
.hero-skyline{position:absolute;right:0;top:0;width:420px;height:324px;background:linear-gradient(90deg,rgba(255,255,255,0),rgba(255,255,255,.06))}
.hero-photo{position:absolute;left:75px;top:0;width:240px;height:324px;background:linear-gradient(#d9b83a 0 14%,#7a6a5a 14% 32%,#4d4d4d 32% 55%,#d9692c 55% 100%);opacity:.7}
.hero h1{position:absolute;left:349px;top:94px;font-size:38px;font-weight:400;color:var(--hero-text);white-space:nowrap}
.hero-copy{position:absolute;left:351px;top:152px;width:580px;font-size:15px;line-height:24px;color:#fff}

.partner{top:552px;width:482px;height:83px;border:1px solid #b7c1cc}
.partner h2{position:absolute;right:20px;top:14px;font-size:19px;font-weight:700;letter-spacing:.5px}
.partner .more{position:absolute;top:45px;height:24px;background:var(--dark);color:#fff;font-size:11px;padding:0 9px;line-height:24px;border-radius:2px}
.p-clean{left:110px;background:linear-gradient(90deg,#6f7c86,#9fb4cb 40%,#a9bfd9)}
.p-clean h2{color:#1e3c44}
.p-civil{left:609px;background:linear-gradient(90deg,#e7c23a 0 20%,#d7d7cf 35%,#b6b6a5);border-color:#bdbdb1}
.p-civil h2{color:#2a2a2a}

.intro-title{left:110px;top:660px;font-size:23px;font-weight:600;color:var(--green)}
.ticks{left:110px;top:700px;list-style:none;font-size:13px;font-weight:600;color:#333;line-height:22px}
.ticks li{display:flex;align-items:center;gap:7px}
.map{left:488px;top:692px;width:195px;height:152px;border-radius:6px;background:linear-gradient(135deg,#b4e070,#8fcc4c)}
.body-copy{left:110px;top:779px;font-size:12px;line-height:20px;color:#555}

.news{left:776px;top:660px;width:314px;height:300px;background:linear-gradient(#f5f5f5,#fff 40%)}
.news-head{height:46px;background:var(--green-light);border:1px solid #bccd6a;font-size:18px;font-weight:600;color:#222;padding:12px 15px}
.news-item{position:absolute;left:15px;display:flex;gap:14px}
.date{width:40px;height:45px;background:var(--green-light);font-size:11px;line-height:15px;text-align:center;padding-top:4px;color:#333;clip-path:polygon(0 0,100% 0,100% 82%,50% 100%,0 82%)}
.news-item h3{font-size:12px;font-weight:700;color:#333;margin-bottom:1px}
.news-item p{font-size:11.5px;line-height:20px;color:#666;width:225px}

.footer{left:0;top:981px;width:1200px;height:64px;background:var(--dark);text-align:center;font-size:12.5px;color:#8a8a8a;padding-top:14px;line-height:20px}
</style>
</head>
<body>
<div class="abs topbar"></div>
<ul class="abs nav">
  <li class="active">Home</li><li>About us</li><li>Company's policy</li><li>History + Certificates</li><li>Map</li><li>Services</li><li>Portfolio</li><li>News/Blog</li><li>Jobs</li><li>Contact us</li>
</ul>

<div class="abs stage"></div>
<div class="abs brand"><span class="brand-mark"></span>VIREO TRADE</div>

<div class="abs search">Enter a keyword...</div>
<div class="abs search-btn">
  <svg width="27" height="28" viewBox="0 0 27 28"><circle cx="12" cy="12" r="6" fill="none" stroke="#fff" stroke-width="2"/><line x1="16.5" y1="16.5" x2="22" y2="22" stroke="#fff" stroke-width="3"/></svg>
</div>
<div class="abs lang">Русский</div>
<div class="abs help">Need Help? Call us on:
  <svg width="20" height="26" viewBox="0 0 20 26"><path d="M6 2c-4 2-4 8 0 14s9 9 11 7" fill="none" stroke="#8aa63a" stroke-width="3" stroke-linecap="round"/></svg>
  <b>+7 812 400 3182</b></div>

<div class="abs hero-frame"></div>
<div class="abs hero">
  <div class="hero-skyline" role="img" aria-label="Dark city skyline with office towers"></div>
  <div class="hero-photo" role="img" aria-label="Engineer in hard hat and safety vest with arms crossed"></div>
  <h1>Quality services on time...</h1>
  <p class="hero-copy">We use an accumulated experience of immovable property maintenance, any kind of engineering systems, and their modernization for extension of durability time, and you save your money.</p>
</div>

<div class="abs partner p-clean" role="img" aria-label="Window cleaner on glass facade">
  <h2>PROFESSIONAL CLEANING</h2><span class="more" style="left:204px">CLICK HERE TO KNOW MORE ›</span>
</div>
<div class="abs partner p-civil" role="img" aria-label="Hard hat on rolled blueprints">
  <h2>CIVIL ENGINEERING</h2><span class="more" style="left:270px">CLICK HERE TO KNOW MORE ›</span>
</div>

<h2 class="abs intro-title">VIREO TM &amp; FM COMPANY</h2>
<ul class="abs ticks">
  <li><svg width="9" height="8"><path d="M1 4l2.5 3L8 1" fill="none" stroke="#6d8a24" stroke-width="2"/></svg>Commercial property management</li>
  <li><svg width="9" height="8"><path d="M1 4l2.5 3L8 1" fill="none" stroke="#6d8a24" stroke-width="2"/></svg>Complex maintenance of immovable property</li>
  <li><svg width="9" height="8"><path d="M1 4l2.5 3L8 1" fill="none" stroke="#6d8a24" stroke-width="2"/></svg>Commercial property maintenance service</li>
</ul>
<div class="abs map" role="img" aria-label="Map of presence across Russia with project locations"></div>
<div class="abs body-copy">
  These are the most important aspects of acquisition of the<br>highest possible incomes from the commercial property object`s<br>operation regardless of their purpose: it can be production,<br>business center, a building of a shop, bank, restaurant,<br><span style="display:block;margin-top:4px">warehousing logistic complex, hotel or the biggest shopping and recreation center.</span>
  <span style="display:block;margin-top:20px">More and more modern companies – proprietors and developer companies, hand over maintenance of the<br>buildings, structures with all installation for outsourcing to a professional management company.</span>
</div>

<section class="abs news">
  <div class="news-head">NEWS</div>
  <div class="news-item" style="top:62px"><div class="date">SEP<br>12</div><div><h3>Lorem ipsum dolor sit amet,</h3><p>Consectetuer adipiscing elit, sed diam nonummy nibh euismod tincidunt ut.</p></div></div>
  <div class="news-item" style="top:142px"><div class="date">SEP<br>10</div><div><h3>Laoreet dolore magna aliquam erat</h3><p>Ut wisi enim ad minim veniam, quis nostrud exerci tation ullamcorper.</p></div></div>
  <div class="news-item" style="top:222px"><div class="date">SEP<br>5</div><div><h3>Suscipit lobortis nisl ut aliquip ex ea</h3><p>Commodo consequat. Duis autem vel eum iriure dolor in hendrerit.</p></div></div>
</section>

<footer class="abs footer">
  Home :: About us :: Company's policy :: History + Certificates :: Services :: Portfolio :: News/blog :: Jobs :: Contact us<br>© Vireo Trade 2010
</footer>
</body>
</html>
```